Community grantmaker building brochure site

The Selvane Community Trust is a grant-making agency that seeks to build an emotionally engaging and informative site that portrays Haiti from an asset lens. We want to focus on the opportunities for growth while highlighting the current opportunity to give to a worthy cause.

Users will be Haitians, Friends of Haiti, and Media who are potential donors, innovators and decision makers.

We envision a home page with a horizontal navigation bar (with About us, Impact/Our work/Projects, Donate, Contact us, Meet the team, and Haiti’s assets/facts/resources/research) a series of large horizontal images (with dissolving motion) and language underneath the image that describes who we are and what we do.

We currently have content for the tabs below:

About us: Selvane Community Trust - The Trust is the country’s first endowed fund building on Haiti’s assets while providing resources for scalable solutions.

The Trust addresses three essential pillars for a thriving Ayiti: environment, entrepreneurship, and civic education. We will invest in water resources focusing in an integrative and systemic way on the lasting impact of this approach.

Donate: A link to the Corvell Foundation and statement about Hurricane Bertrand. “Giving for Outcomes”

Sustainable Funding: Links to articles and resources that show our theory of change while highlighting facts about Haiti.

Meet the team: A list of names and images of the board

Also in the same frame we would like 3 tiles titled The Environment, Entrepreneurship, Civic Engagement with an option to scroll over for additional information.

Lastly the link to donate should be featured prominently and several times along with cues that lead people to find out more about the facts and the Sustainable Funding page.

We prefer limited scrolling and would like to see a clean yet modern approach to this funding platform.

Thank you and looking forward!
Updates

Project Deadline Extended
Reason: Thank you! Our executive board has rescheduled our meeting so we'll need a few more days to coordinate. Much appreciated.

Target Market(s)

Haitians, Friends of Haiti, and Media who are potential donors, innovators and decision makers

Industry/Entity Type

Foundation

Coding

Coded - Design and coding required

Number of Pages Required

5+ page

Requirements
Must have
• emotionally engaging and informative
• asset-focused language
• motion enabled pictures
• links to donate
Nice to have
• scoll-over and pop-ups
• music
Should not have
• charity language
• denigrating language
• images that depict poverty or need

```html
<!DOCTYPE html>
<html lang="en">
<head>
<meta charset="utf-8">
<title>Selvane Community Trust</title>
<link href="https://fonts.googleapis.com/css2?family=Open+Sans:wght@400;600;700&family=PT+Sans:wght@400;700&display=swap" rel="stylesheet">
<style>
:root{
  --red:#c4202d;
  --red-dark:#a81824;
  --blue:#1e4f8f;
  --text:#555a60;
  --muted:#7a7f85;
  --line:#e4e6ea;
  --yellow-top:#ffd84a;
  --yellow-bot:#f5b400;
  --white:#ffffff;
  --band:#f1f2f4;
}
*{box-sizing:border-box;margin:0;padding:0}
html,body{width:1200px;height:2990px;overflow:hidden}
body{position:relative;font-family:"Open Sans",Arial,sans-serif;color:var(--text);background:var(--white)}
.abs{position:absolute}
h1,h2,h3,h4{font-weight:400}

/* header */
.brand{left:40px;top:34px;display:flex;align-items:center;gap:14px}
.brand-dot{width:60px;height:60px;border:3px solid var(--red);border-radius:50%}
.brand-name{font-family:"PT Sans",sans-serif;font-weight:700;font-size:27px;color:var(--red);letter-spacing:.5px}
.social{left:640px;top:32px;display:flex;align-items:center;gap:6px;font-size:12px;color:#333}
.social span.c{width:28px;height:28px;border-radius:50%;display:inline-block}
.social .lbl{margin-right:8px}
.top-donate{left:1028px;top:20px;width:106px;height:40px;border-radius:4px;background:linear-gradient(var(--yellow-top),var(--yellow-bot));box-shadow:0 2px 3px rgba(0,0,0,.2);display:flex;align-items:center;justify-content:center;gap:8px;font-weight:700;font-size:15px;color:#3a2c00}
.top-donate i{width:10px;height:10px;border-radius:50%;background:var(--red);display:inline-block}
.nav{top:84px;left:0;width:1200px;height:22px}
.nav a{position:absolute;transform:translateX(-50%);font-size:14px;color:#444;text-decoration:none;white-space:nowrap}

/* hero */
.hero-photo{left:0;top:126px;width:600px;height:610px;background:linear-gradient(160deg,#7f9f5a 0%,#4f7a3a 45%,#2c3f22 100%)}
.hero-title{left:40px;top:614px;font-weight:700;font-size:37px;color:var(--white);text-shadow:0 2px 6px rgba(0,0,0,.4)}
.hero-sub{left:40px;top:666px;font-size:19px;color:var(--white);letter-spacing:.3px}
.arrow{top:696px;width:26px;height:26px;border:1px solid rgba(255,255,255,.8);background:rgba(0,0,0,.35);display:flex;align-items:center;justify-content:center}
.hero-panel{left:600px;top:126px;width:600px;height:610px;background:var(--red)}
.hero-panel h2{position:absolute;top:226px;width:100%;text-align:center;color:var(--white);font-size:32px;font-family:"PT Sans",sans-serif}
.hero-panel p{position:absolute;left:96px;top:290px;width:412px;text-align:center;color:#fbe3e5;font-size:12.5px;line-height:2.15}
.hero-donate{left:760px;top:582px;width:284px;height:74px;border-radius:3px;background:linear-gradient(var(--yellow-top),var(--yellow-bot));box-shadow:0 3px 5px rgba(0,0,0,.25)}
.hero-donate .ring{position:absolute;left:18px;top:17px;width:40px;height:40px;border:3px solid var(--red);border-radius:50%}
.hero-donate b{position:absolute;left:74px;top:8px;font-size:24px;color:#4a3a06}
.hero-donate small{position:absolute;left:74px;top:42px;font-size:13px;color:#4a3a06}

/* pillars */
.pillar{top:822px;width:320px;text-align:center}
.pillar .icon{width:118px;height:118px;margin:0 auto;border-radius:50%;display:flex;align-items:center;justify-content:center}
.pillar h3{margin-top:30px;font-size:17px;color:var(--blue)}
.pillar p{margin:14px auto 0;width:290px;font-size:11.5px;line-height:2;color:var(--muted)}

/* projects */
.section-title{width:1200px;left:0;text-align:center;font-family:"PT Sans",sans-serif;font-size:31px;color:var(--blue)}
.rule{width:50px;height:2px;left:575px}
.intro{left:180px;width:840px;text-align:center;font-size:11.5px;line-height:2.1;color:var(--muted)}
.card{top:1306px;width:236px;height:320px}
.card .cap{position:absolute;left:14px;bottom:20px;width:200px;padding-left:14px;border-left:3px solid var(--red);font-size:12.5px;line-height:1.7;color:var(--white)}
.btn-red{background:var(--red);color:var(--white);font-size:14px;display:flex;align-items:center;justify-content:center;border-radius:2px}

/* about band */
.about-band{left:0;top:1802px;width:1200px;height:424px;background:linear-gradient(180deg,#2b2f49 0%,#5a5662 35%,#a07a55 65%,#b9875a 100%)}
.about-text{left:190px;top:1976px;width:820px;text-align:center;color:#f3ece4;font-size:12.5px;line-height:2.2}

/* testimonials */
.quote{top:2400px;width:320px}
.quote .mark{position:absolute;font-family:Georgia,serif;font-size:38px;color:#bfc3c8;line-height:1}
.quote p{margin-left:24px;width:250px;font-size:12.5px;line-height:2;color:#555}
.person{top:2536px;display:flex;align-items:center;gap:16px}
.person .av{width:56px;height:56px;border-radius:50%;border:2px solid var(--blue);background:radial-gradient(circle at 50% 40%,#d9b39a,#8f6a55)}
.person b{display:block;font-size:12px;color:var(--red);text-transform:uppercase;font-weight:600}
.person small{font-size:11px;color:var(--muted)}

/* footer */
.footer-line{left:0;top:2680px;width:1200px;height:1px;background:var(--line)}
.f-title{font-family:"PT Sans",sans-serif;font-size:17px;color:#222}
.f-text{font-size:12px;line-height:2;color:#555}
.f-links a{display:block;font-size:12px;color:#555;text-decoration:none;line-height:26px}
.partner{left:884px;top:2738px;width:230px;font-family:"PT Sans",sans-serif;font-weight:700;font-size:32px;line-height:1.05;color:#8c8f94}
.copy{left:0;top:2924px;width:1200px;height:66px;background:var(--band);border-top:1px solid var(--line);display:flex;align-items:center;justify-content:center;font-size:12px;color:#555}
</style>
</head>
<body>

<!-- Header -->
<header>
  <div class="abs brand"><span class="brand-dot"></span><span class="brand-name">SELVANE COMMUNITY TRUST</span></div>
  <div class="abs social">
    <span class="lbl">Connect with our social network :</span>
    <span class="c" style="background:#3b5ca8"></span>
    <span class="c" style="background:#3fa9e0"></span>
    <span class="c" style="background:#d2232a"></span>
    <span class="c" style="background:#222"></span>
    <span class="c" style="background:#1d75a6"></span>
  </div>
  <div class="abs top-donate">Donate <i></i></div>
  <nav class="abs nav">
    <a style="left:420px">Home</a>
    <a style="left:516px">About us</a>
    <a style="left:618px">Impact</a>
    <a style="left:714px">Donate</a>
    <a style="left:822px">Contact us</a>
    <a style="left:952px">Meet the team</a>
    <a style="left:1092px">Haiti’s assets</a>
  </nav>
</header>

<!-- Hero -->
<section>
  <div class="abs hero-photo" role="img" aria-label="Photo of a smiling man standing in a green sugar cane field"></div>
  <h1 class="abs hero-title">Scalable Solutions for Haiti</h1>
  <div class="abs hero-sub">Enviroment | Entrepreneueship | Civic Education</div>
  <div class="abs arrow" style="left:530px"><svg width="10" height="12" viewBox="0 0 10 12"><path d="M7 1L2 6l5 5" stroke="#fff" stroke-width="2" fill="none"/></svg></div>
  <div class="abs arrow" style="left:572px"><svg width="10" height="12" viewBox="0 0 10 12"><path d="M3 1l5 5-5 5" stroke="#fff" stroke-width="2" fill="none"/></svg></div>
  <div class="abs hero-panel">
    <h2>Selvane Community Trust</h2>
    <p>Lorem Ipsum is simply dummy text of the printing and typesetting industry. Lorem Ipsum has been the industry’s standard dummy text ever since the 1500s, when an unknown printer took a galley of type and scrambled it to make a type specimen book. It has survived not only five centuries</p>
  </div>
  <div class="abs hero-donate"><span class="ring"></span><b>Donate</b><small>Lorem Ipsum is simply dummy</small></div>
</section>

<!-- Pillars -->
<section>
  <div class="abs pillar" style="left:96px">
    <div class="icon" style="border:2px solid var(--red);box-shadow:inset 0 0 0 6px #fff,inset 0 0 0 7px var(--red)">
      <svg width="44" height="44" viewBox="0 0 44 44"><path d="M22 40V22M22 24C10 22 8 12 10 6c8 2 14 8 12 18zM22 26c10-2 14-8 12-16-8 2-12 8-12 16z" fill="var(--red)" stroke="var(--red)" stroke-width="2"/></svg>
    </div>
    <h3>Enviroment</h3>
    <p>Lorem Ipsum is simply dummy text of the printing and typesetting industry. Lorem Ipsum has been the industry’s standard dummy...</p>
  </div>
  <div class="abs pillar" style="left:440px">
    <div class="icon" style="border:2px solid var(--blue);box-shadow:inset 0 0 0 6px #fff,inset 0 0 0 7px var(--blue)">
      <svg width="48" height="48" viewBox="0 0 48 48" fill="none" stroke="var(--blue)" stroke-width="2"><path d="M24 12a10 10 0 0 0-6 18v4h12v-4a10 10 0 0 0-6-18z"/><path d="M19 38h10M21 42h6M24 2v5M8 8l4 4M40 8l-4 4M4 22h5M39 22h5"/></svg>
    </div>
    <h3>Entrepreneueship</h3>
    <p>Lorem Ipsum is simply dummy text of the printing and typesetting industry. Lorem Ipsum has been the industry’s standard dummy...</p>
  </div>
  <div class="abs pillar" style="left:784px">
    <div class="icon" style="border:2px solid var(--blue);box-shadow:inset 0 0 0 6px #fff,inset 0 0 0 7px var(--blue)">
      <svg width="48" height="48" viewBox="0 0 48 48"><circle cx="24" cy="12" r="6" fill="var(--blue)"/><path d="M6 22c8 0 14 2 18 6 4-4 10-6 18-6v18c-8 0-14 2-18 6-4-4-10-6-18-6z" fill="var(--blue)"/><path d="M24 28v18" stroke="#fff" stroke-width="2"/></svg>
    </div>
    <h3>Civic Education</h3>
    <p>Lorem Ipsum is simply dummy text of the printing and typesetting industry. Lorem Ipsum has been the industry’s standard dummy...</p>
  </div>
</section>

<!-- Projects -->
<section>
  <h2 class="abs section-title" style="top:1128px">Our Projects</h2>
  <div class="abs rule" style="top:1184px;background:var(--blue)"></div>
  <p class="abs intro" style="top:1210px">Lorem Ipsum is simply dummy text of the printing and typesetting industry. Lorem Ipsum has been the industry’s standard dummy text ever since the 1500s, when an unknown printer took a galley of type and scrambled it to make a type specimen book...</p>
  <div class="abs card" style="left:100px;background:linear-gradient(180deg,#d8d2c8,#a8a39a 60%,#6f6a63)" role="img" aria-label="Photo of a smiling family group of women and a girl"><div class="cap">Lorem Ipsum is simply dummy text of the printing</div></div>
  <div class="abs card" style="left:356px;background:linear-gradient(180deg,#b9c4cf,#8a8f8a 45%,#6b5a3e)" role="img" aria-label="Photo of a hiker walking toward a mountain"><div class="cap">Lorem Ipsum is simply dummy text of the printing</div></div>
  <div class="abs card" style="left:612px;background:linear-gradient(180deg,#3a3c40,#1d1e21 60%,#4a4b4f)" role="img" aria-label="Photo of a video camera"><div class="cap">Lorem Ipsum is simply dummy text of the printing</div></div>
  <div class="abs card" style="left:868px;background:linear-gradient(180deg,#e6e2dc,#b6b1ab 50%,#8e98a8)" role="img" aria-label="Photo of a woman with glasses in a light room"><div class="cap">Lorem Ipsum is simply dummy text of the printing</div></div>
  <div class="abs btn-red" style="left:508px;top:1680px;width:188px;height:44px">View more Projects</div>
</section>

<!-- About -->
<section>
  <div class="abs about-band" role="img" aria-label="Photo of desert sand dunes under a hazy evening sky"></div>
  <h2 class="abs section-title" style="top:1886px;color:var(--white)">About Selvane Community Trust</h2>
  <div class="abs rule" style="top:1948px;background:var(--white)"></div>
  <p class="abs about-text">Lorem Ipsum is simply dummy text of the printing and typesetting industry. Lorem Ipsum has been the industry’s standard dummy text ever since the 1500s, when an unknown printer took a galley of type and scrambled it to make a type specimen book. It has survived not only five centuries, but also the leap into electronic typesetting, remaining essentially unchanged...</p>
  <div class="abs btn-red" style="left:524px;top:2086px;width:156px;height:44px">View more info</div>
</section>

<!-- Testimonials -->
<section>
  <h2 class="abs section-title" style="top:2316px">Testimonials</h2>
  <div class="abs rule" style="top:2376px;background:var(--blue)"></div>

  <div class="abs quote" style="left:100px">
    <span class="mark" style="left:0;top:0">“</span><span class="mark" style="left:296px;top:80px">”</span>
    <p style="margin-top:10px">Lorem Ipsum is simply dummy text of the printing and typesetting industry. Lorem Ipsum has been the industry’s standard dummy text ever since the 1500s...</p>
  </div>
  <div class="abs quote" style="left:446px">
    <span class="mark" style="left:0;top:0">“</span><span class="mark" style="left:296px;top:80px">”</span>
    <p style="margin-top:10px">Lorem Ipsum is simply dummy text of the printing and typesetting industry. Lorem Ipsum has been the industry’s standard dummy text ever since the 1500s...</p>
  </div>
  <div class="abs quote" style="left:792px">
    <span class="mark" style="left:0;top:0">“</span><span class="mark" style="left:296px;top:80px">”</span>
    <p style="margin-top:10px">Lorem Ipsum is simply dummy text of the printing and typesetting industry. Lorem Ipsum has been the industry’s standard dummy text ever since the 1500s...</p>
  </div>

  <div class="abs person" style="left:106px"><span class="av" role="img" aria-label="Portrait photo of a reviewer"></span><div><b>Marcel Dorval</b><small>Business man</small></div></div>
  <div class="abs person" style="left:452px"><span class="av" role="img" aria-label="Portrait photo of a reviewer"></span><div><b>Marcel Dorval</b><small>Business man</small></div></div>
  <div class="abs person" style="left:798px"><span class="av" role="img" aria-label="Portrait photo of a reviewer"></span><div><b>Marcel Dorval</b><small>Business man</small></div></div>
</section>

<!-- Footer -->
<footer>
  <div class="abs footer-line"></div>
  <h4 class="abs f-title" style="left:100px;top:2726px">Privacy Policy</h4>
  <p class="abs f-text" style="left:100px;top:2760px;width:300px">Lorem Ipsum is simply dummy text of the printing and typesetting industry. Lorem Ipsum has been the industry’s standard dummy text ever since the 1500s</p>
  <div class="abs btn-red" style="left:100px;top:2846px;width:108px;height:34px;font-size:13px">Read more</div>

  <h4 class="abs f-title" style="left:472px;top:2726px">Welcome</h4>
  <div class="abs f-links" style="left:474px;top:2758px">
    <a>Impact</a><a>Donate</a><a>Contact us</a><a>Meet the team</a><a>Haiti’s assets</a>
  </div>

  <h4 class="abs f-title" style="left:636px;top:2726px">Contact Info</h4>
  <p class="abs f-text" style="left:640px;top:2760px;width:200px;line-height:22px">120 Street name, City name,<br>Country name : 0000000</p>
  <div class="abs f-text" style="left:640px;top:2804px;display:flex;align-items:center;gap:8px">
    <svg width="12" height="12" viewBox="0 0 12 12"><path d="M2 1l2.5 0 1 3-1.5 1a7 7 0 0 0 3 3l1-1.5 3 1V10a1 1 0 0 1-1 1A9 9 0 0 1 1 2a1 1 0 0 1 1-1z" fill="var(--red)"/></svg>
    ( 555 ) 014 - 2207
  </div>
  <div class="abs f-text" style="left:640px;top:2832px;display:flex;align-items:center;gap:8px">
    <svg width="13" height="10" viewBox="0 0 13 10"><rect x=".5" y=".5" width="12" height="9" fill="none" stroke="var(--red)"/><path d="M.5 .5l6 5 6-5" fill="none" stroke="var(--red)"/></svg>
    info@selvanecommunitytrust.org
  </div>

  <div class="abs partner">Corvell Foundation</div>

  <div class="abs copy">Copyright © 2016. Selvane Community Trust. All Rights Reserved</div>
</footer>

</body>
</html>
```